Popup Nightclub Grand Opening Flyer

We need to design a flyer for the grand opening of an upscale, exclusive nightclub called "Lanternfall". The design needs to be chic and exclusive. The background should be black and the text should primarily be white. We like minimalist designs.

Here is the text for the flyer
-
Velvetrope Atlanta Presents

Lanternfall (LOGO)

A Popup Nightclub Experience
For one night Only

Friday, October 18, 2013
Party begins at 9PM

INVITE ONLY

See invitation for location details
(Velvetrope Atlanta logo)

-
Examples we like

http://cdn2-b.brivelpost.com/sites/default/files/styles/image_content_width/hash/3d/fa/1472093815_4471_flyer.jpg?itok=R8kqWm2z

http://api.plovra.com/files/7Kqq-Tr82XXB3pQzJvmtR5HL2W719E4nbRtC6KLd4HsfM8Y2qTDK-VmjwDoNqLX4QBzTHD9nakRbVx3m-Pfq8htc3MDTWr5p4/2zelSaturdays.jpg

http://quenmar.com/wp-content/uploads/yootheme/widgetkit/gallery/2zel/2zel-gen_vroom4-01.jpg

Hi All, one thing that we are seeing that we don't like is on over emphasis on the phrase "a popup nightclub experience" please don't make this the largest thing on the flyer

Target Market(s)

Target market is 25-35 year olds who are affluent (rich) and like luxury brands

Requirements
Must have
• Dark Background
Nice to have
• Velvetrope Logo on the bottom
Modern text that isn't curvy
Should not have
• Curved text

```html
<!DOCTYPE html>
<html lang="en">
<head>
<meta charset="utf-8">
<title>Velvetrope Atlanta Presents Lanternfall Nightclub</title>
<link rel="stylesheet" href="https://fonts.googleapis.com/css2?family=Montserrat:wght@300&family=Tinos&display=swap">
<style>
  :root {
    --bg: #000000;
    --ink: #ffffff;
    --ink-soft: #e4e4e4;
    --mark: #bdbdbd;
    --rule: #8a8a8a;
    --glow: rgba(255, 255, 255, 0.55);
  }
  * { margin: 0; padding: 0; box-sizing: border-box; }
  html, body {
    width: 927px;
    height: 1200px;
    overflow: hidden;
    background: var(--bg);
  }
  .flyer {
    position: relative;
    width: 927px;
    height: 1200px;
    background: var(--bg);
    color: var(--ink);
    font-family: "Tinos", "Times New Roman", serif;
  }
  .line {
    position: absolute;
    left: 0;
    width: 100%;
    text-align: center;
    white-space: nowrap;
  }
  .presenter {
    top: 62px;
    font-family: "Montserrat", Arial, sans-serif;
    font-weight: 300;
    font-size: 54px;
    letter-spacing: 6px;
    color: var(--ink);
  }
  .club-mark {
    position: absolute;
    left: 50%;
    top: 212px;
    transform: translateX(-50%);
  }
  .club-name {
    top: 420px;
    font-family: "Montserrat", Arial, sans-serif;
    font-weight: 300;
    font-size: 52px;
    letter-spacing: 8px;
    color: var(--ink-soft);
  }
  .club-type {
    top: 484px;
    font-family: "Montserrat", Arial, sans-serif;
    font-weight: 300;
    font-size: 26px;
    letter-spacing: 5px;
    color: var(--ink-soft);
  }
  .rule {
    position: absolute;
    left: 114px;
    width: 730px;
    height: 1px;
    background: var(--rule);
  }
  .rule--upper { top: 550px; }
  .rule--lower { top: 923px; }
  .detail {
    font-size: 34px;
    color: var(--ink);
    text-shadow: 0 0 6px var(--glow), 0 0 2px var(--glow);
  }
  .tagline { top: 598px; }
  .duration { top: 686px; }
  .date {
    position: absolute;
    left: 176px;
    top: 792px;
    font-size: 38px;
    line-height: 1;
    color: var(--ink);
    text-shadow: 0 0 6px var(--glow), 0 0 2px var(--glow);
    white-space: nowrap;
  }
  .start {
    position: absolute;
    left: 230px;
    top: 836px;
    font-size: 38px;
    line-height: 1;
    color: var(--ink);
    text-shadow: 0 0 6px var(--glow), 0 0 2px var(--glow);
    white-space: nowrap;
  }
  .access { top: 948px; font-size: 38px; }
  .location { top: 1028px; font-size: 30px; }
  .host {
    position: absolute;
    left: 0;
    top: 1102px;
    width: 100%;
    display: flex;
    justify-content: center;
    align-items: center;
    gap: 22px;
  }
  .host-dot {
    width: 46px;
    height: 46px;
    border-radius: 50%;
    background: var(--mark);
  }
  .host-name {
    font-family: "Montserrat", Arial, sans-serif;
    font-weight: 300;
    font-size: 40px;
    letter-spacing: 5px;
    color: var(--ink);
  }
</style>
</head>
<body>
  <main class="flyer">
    <p class="line presenter">VELVETROPE PRESENTS</p>

    <svg class="club-mark" width="150" height="150" viewBox="0 0 150 150" aria-hidden="true">
      <circle cx="75" cy="75" r="74" fill="var(--mark)"/>
    </svg>
    <h1 class="line club-name">LANTERNFALL</h1>
    <p class="line club-type">NIGHTCLUB</p>

    <div class="rule rule--upper"></div>

    <p class="line detail tagline">A POPUP NIGHTCLUB EXPERIENCE</p>
    <p class="line detail duration">FOR ONE NIGHT ONLY</p>
    <p class="date">FRIDAY, OCTOBER 18TH, 2013</p>
    <p class="start">PARTY BEGINS AT 9PM</p>

    <div class="rule rule--lower"></div>

    <p class="line detail access">INVITE ONLY</p>
    <p class="line detail location">SEE INVITATION FOR LOCATION DETAILS</p>

    <div class="host">
      <span class="host-dot" aria-hidden="true"></span>
      <span class="host-name">VELVETROPE ATLANTA</span>
    </div>
  </main>
</body>
</html>
```